Presentation Of Our Epidemiology Consulting Framework

We need a slide deck (png files) for PowerPoint that describes our organization and type of clients we serve, and our 6 phase framework that explains how we work with clients. Please use the minimum amount of text on each slide.  We want a more visual display of how to work with us. We want it to look very similar to our brochure.  We want to also have a few extra branded slides without text that can be used as a template if we decide to add to the deck later or create a new slide deck.
Colors
#56588C
#F28444
#F2E088
#F24C27
#ODODOD

```html
<!DOCTYPE html>
<html lang="en">
<head>
<meta charset="utf-8">
<title>Dr Reyes Health – Framework Deck</title>
<link href="https://fonts.googleapis.com/css2?family=Poppins:wght@400;500;600;700;800&family=Dancing+Script:wght@600&display=swap" rel="stylesheet">
<style>
:root{
  --navy:#24224c;
  --navy-deep:#14132e;
  --indigo:#56588C;
  --violet:#5d5ab0;
  --pill:#3a3989;
  --orange:#F28444;
  --orange-hot:#F24C27;
  --lavender:#e4e3f1;
  --ink:#0D0D0D;
  --white:#ffffff;
  --board:#d8d8d8;
}
*{box-sizing:border-box;margin:0;padding:0}
html,body{width:689px;height:1200px;overflow:hidden;background:var(--board)}
body{font-family:"Poppins",Arial,sans-serif}
.board{position:relative;width:1456px;height:2537px;transform:scale(.4732);transform-origin:0 0}
.slide{position:absolute;width:635px;height:357px;overflow:hidden;background:var(--navy);color:var(--white);box-shadow:0 2px 4px rgba(0,0,0,.12)}
.col-l{left:70px}.col-r{left:751px}
.wave{position:absolute;left:0;bottom:0;width:635px;height:70px}
.brand{position:absolute;right:18px;bottom:10px;display:flex;align-items:center;gap:5px;font-weight:700;font-size:13px;color:var(--violet)}
.brand .dot{width:10px;height:10px;border-radius:50%;background:var(--orange)}
.page-no{position:absolute;left:38px;bottom:5px;font-size:5px;color:var(--lavender)}

/* phase slides */
.phase-tab{position:absolute;left:32px;top:0;width:74px;height:74px;background:var(--orange);border-radius:0 0 37px 37px;text-align:center;padding-top:10px}
.phase-tab .label{display:block;font-weight:800;font-size:14px;line-height:1}
.phase-tab .num{display:block;font-weight:800;font-size:36px;line-height:1.05;color:var(--navy)}
.phase-icon{position:absolute;left:32px;top:96px;width:50px;height:50px;border-radius:50%;background:var(--white)}
.phase-icon svg{width:50px;height:50px}
.phase-title{position:absolute;left:32px;top:148px;width:220px}
.phase-title h2{font-weight:800;font-size:26px;line-height:31px}
.phase-title p{font-weight:700;font-size:16.5px;line-height:20px;color:var(--orange);margin-top:6px}
.steps{position:absolute;left:268px;width:336px;list-style:none}
.steps li{position:absolute;left:0;width:336px;height:48px;border-radius:24px;background:var(--pill);display:flex;align-items:center;gap:8px;padding-left:10px;font-size:13px;line-height:17px}
.steps.five li{height:40px}
.steps li svg{flex:none;width:18px;height:18px}
.steps-intro{position:absolute;left:268px;top:22px;font-size:11.5px;font-weight:700}

/* cover */
.cover{background:linear-gradient(110deg,#15142f 0%,#2a2860 45%,#6a67b6 100%)}
.cover .photo{position:absolute;left:330px;top:0;width:305px;height:357px;background:linear-gradient(180deg,#5f5ca8 0%,#3a3870 55%,#25234a 100%)}
.logo-top{position:absolute;left:30px;top:44px;display:flex;align-items:center;gap:6px;font-weight:700;font-size:19px;color:var(--violet)}
.logo-top .dot{width:14px;height:14px;border-radius:50%;background:var(--orange)}
.cover .script{position:absolute;left:32px;top:94px;font-family:"Dancing Script",cursive;font-size:24px;color:var(--orange)}
.cover h1{position:absolute;left:32px;top:126px;font-weight:800;font-size:27px;line-height:35px}
.cover .tag{position:absolute;left:32px;top:206px;width:188px;height:25px;border-radius:13px;background:var(--orange);font-weight:700;font-size:15px;line-height:25px;text-align:center}
.cover .framework{position:absolute;left:32px;top:236px;font-weight:800;font-size:29px;color:#6f6cd0;letter-spacing:.5px}
.contact{position:absolute;display:flex;align-items:center;gap:6px;font-size:10px}
.contact .ic{width:16px;height:16px;border-radius:50%;background:var(--orange);display:flex;align-items:center;justify-content:center}
.cover .contact{left:32px;top:309px}

/* about */
.about{background:var(--lavender);color:var(--ink)}
.about .panel{position:absolute;left:0;top:36px;width:260px;height:321px;background:var(--navy);border-radius:0 60px 0 0}
.about .photo{position:absolute;left:20px;top:18px;width:265px;height:339px;background:linear-gradient(180deg,#8a88b8 0%,#4b4970 50%,#2b2a48 100%)}
.about .intro{position:absolute;left:293px;top:34px;width:320px;font-size:10.5px;line-height:13px}
.about .intro b{font-weight:700}
.about .approach{position:absolute;left:280px;top:193px;width:355px;height:121px;background:var(--indigo);color:var(--white);padding:12px 12px 0 13px}
.about .approach h3{font-weight:700;font-size:16px;color:var(--orange)}
.about .approach p{font-size:8.8px;line-height:13px;margin-top:3px}

/* why partner */
.why h2{position:absolute;left:32px;top:132px;font-weight:800;font-size:26px;line-height:31px}
.why h2 span{color:var(--orange)}
.point{position:absolute;font-size:10px;line-height:13px}
.point b{display:block;color:var(--orange);font-size:13px;font-weight:700;line-height:16px}
.point.right-al{text-align:right}
.why2 .band{position:absolute;left:0;top:60px;width:220px;height:217px;background:var(--pill);border-radius:0 108px 108px 0}
.bubble{position:absolute;width:40px;height:40px;border-radius:50%;background:var(--orange);border:2px solid var(--navy);display:flex;align-items:center;justify-content:center}
.bubble svg{width:22px;height:22px}

/* closing */
.closing{background:linear-gradient(180deg,#2a2860 0%,#14132e 100%)}
.closing .arc{position:absolute;left:345px;top:0;width:500px;height:520px;border-radius:50%;background:rgba(70,68,140,.35)}
.closing .logo-top{top:46px}
.closing h2{position:absolute;left:32px;top:118px;font-weight:800;font-size:28px;line-height:34px}
.closing h2 span{color:var(--orange)}
.closing .cta{position:absolute;left:397px;top:122px;width:220px;font-size:15.5px;line-height:19px}
.closing .contact{left:397px;top:206px;height:22px;width:188px;background:var(--orange);border-radius:11px;padding-left:3px;font-weight:700;font-size:10px}
.closing .contact .ic{background:var(--white)}

/* template */
.template h2{position:absolute;left:32px;top:32px;font-weight:800;font-size:18px}
.columns{position:absolute;left:32px;top:70px;display:flex;gap:19px}
.col{width:178px}
.col p{font-size:8.3px;line-height:11.5px}
.col p b{color:var(--orange);font-weight:700}
.quote{margin-top:9px;height:56px;border-radius:0 0 8px 8px;background:var(--pill);padding:8px 8px 0 8px;display:flex;gap:6px;font-size:8.3px;line-height:11px;font-style:italic}
.quote .mark{color:var(--orange);font-size:20px;font-weight:800;font-style:normal;line-height:16px}
.quote-by{text-align:right;margin-top:6px;margin-right:6px;font-size:8.5px;font-weight:700;color:var(--orange)}
</style>
</head>
<body>
<svg width="0" height="0" style="position:absolute">
  <defs>
    <symbol id="tick" viewBox="0 0 18 18"><circle cx="9" cy="9" r="7.5" fill="none" stroke="#F28444" stroke-width="1.4"/><path d="M5.5 9.2l2.3 2.3 4.5-4.6" fill="none" stroke="#F28444" stroke-width="1.5" stroke-linecap="round" stroke-linejoin="round"/></symbol>
    <symbol id="wave" viewBox="0 0 635 70"><path d="M0 64 Q330 52 635 16 L635 70 L0 70Z" fill="#e4e3f1"/><path d="M0 62 Q330 48 635 12" fill="none" stroke="#5d5ab0" stroke-width="3"/></symbol>
    <symbol id="mail" viewBox="0 0 10 8"><rect x=".5" y=".5" width="9" height="7" rx="1" fill="none" stroke="#fff"/><path d="M.8 1l4.2 3.2L9.2 1" fill="none" stroke="#fff"/></symbol>
    <symbol id="people" viewBox="0 0 24 24"><circle cx="12" cy="8" r="3" fill="none" stroke="currentColor" stroke-width="1.4"/><path d="M6 19c0-4 3-6 6-6s6 2 6 6" fill="none" stroke="currentColor" stroke-width="1.4"/><circle cx="5" cy="10" r="2" fill="none" stroke="currentColor" stroke-width="1.2"/><circle cx="19" cy="10" r="2" fill="none" stroke="currentColor" stroke-width="1.2"/></symbol>
    <symbol id="target" viewBox="0 0 24 24"><circle cx="12" cy="12" r="8" fill="none" stroke="currentColor" stroke-width="1.4"/><circle cx="12" cy="12" r="4" fill="none" stroke="currentColor" stroke-width="1.4"/><circle cx="12" cy="12" r="1.2" fill="currentColor"/></symbol>
    <symbol id="hands" viewBox="0 0 24 24"><path d="M3 11l4-4 5 3 5-3 4 4-5 5-4-3-4 3z" fill="none" stroke="currentColor" stroke-width="1.4" stroke-linejoin="round"/></symbol>
    <symbol id="bulb" viewBox="0 0 24 24"><path d="M12 4a5 5 0 0 0-3 9v3h6v-3a5 5 0 0 0-3-9z" fill="none" stroke="currentColor" stroke-width="1.4"/><path d="M9.5 19h5" stroke="currentColor" stroke-width="1.4"/></symbol>
  </defs>
</svg>

<div class="board">

  <!-- Cover -->
  <section class="slide col-l cover" style="top:90px">
    <div class="photo" role="img" aria-label="Portrait photo of the firm's founder"></div>
    <div class="logo-top"><span class="dot"></span>Dr Reyes Health</div>
    <div class="script">Transforming</div>
    <h1>Health Data into<br>Community Impact</h1>
    <div class="tag">The Dr Reyes Health</div>
    <div class="framework">FRAMEWORK</div>
    <div class="contact"><span class="ic"><svg width="9" height="7"><use href="#mail"/></svg></span>support@drreyeshealth.com</div>
  </section>

  <!-- About -->
  <section class="slide col-r about" style="top:90px">
    <div class="panel"></div>
    <div class="photo" role="img" aria-label="Portrait photo of the founder holding glasses"></div>
    <p class="intro"><b>Dr Reyes Health LLC</b> is an epidemiology consulting firm that supports large nonprofit organizations and government agencies that serve black, indigenous, and people of color commonly referred to as BIPOC communities. Our diverse team of innovative global public health professionals are ready to serve your organization by helping you address your most pressing challenges.</p>
    <div class="approach">
      <h3>Our Approach</h3>
      <p>At Dr Reyes Health LLC, we believe in transforming health data into actionable insights for BIPOC communities. Our proven six-phase partnership model ensures your organization's success in communicating vital health information effectively.</p>
    </div>
    <div class="brand"><span class="dot"></span>Dr Reyes Health</div>
  </section>

  <!-- Phase 1 -->
  <section class="slide col-l" style="top:487px">
    <div class="phase-tab"><span class="label">PHASE</span><span class="num">1</span></div>
    <div class="phase-icon"><svg viewBox="0 0 50 50"><circle cx="22" cy="22" r="9" fill="none" stroke="#F28444" stroke-width="2.5"/><path d="M29 29l8 8" stroke="#56588C" stroke-width="3.5" stroke-linecap="round"/></svg></div>
    <div class="phase-title"><h2>Discovery<br>&amp; Vision<br>Alignment</h2><p>Building<br>the Foundation<br>for Success</p></div>
    <ul class="steps">
      <li style="top:47px"><svg><use href="#tick"/></svg>Deep-dive exploration of your organization's<br>unique challenges and opportunities</li>
      <li style="top:106px"><svg><use href="#tick"/></svg>Strategic alignment of goals and<br>expectations</li>
      <li style="top:164px"><svg><use href="#tick"/></svg>Custom-tailored solution design</li>
      <li style="top:223px"><svg><use href="#tick"/></svg>Clear roadmap development<br>with defined milestones</li>
    </ul>
    <svg class="wave"><use href="#wave"/></svg><span class="page-no">3</span>
    <div class="brand"><span class="dot"></span>Dr Reyes Health</div>
  </section>

  <!-- Phase 2 -->
  <section class="slide col-r" style="top:487px">
    <div class="phase-tab"><span class="label">PHASE</span><span class="num">2</span></div>
    <div class="phase-icon" style="color:#56588C"><svg viewBox="-13 -13 50 50"><use href="#hands"/></svg></div>
    <div class="phase-title"><h2>Partnership<br>Launch</h2><p>Setting the Stage<br>for Excellence</p></div>
    <ul class="steps five">
      <li style="top:46px"><svg><use href="#tick"/></svg>Formation of dedicated project team</li>
      <li style="top:96px"><svg><use href="#tick"/></svg>Establishment of collaborative workflow</li>
      <li style="top:145px"><svg><use href="#tick"/></svg>Comprehensive data gathering</li>
      <li style="top:196px"><svg><use href="#tick"/></svg>Strategic timeline planning</li>
      <li style="top:246px"><svg><use href="#tick"/></svg>Stakeholder engagement and vision capture</li>
    </ul>
    <svg class="wave"><use href="#wave"/></svg><span class="page-no">4</span>
    <div class="brand"><span class="dot"></span>Dr Reyes Health</div>
  </section>

  <!-- Phase 3 -->
  <section class="slide col-l" style="top:883px">
    <div class="phase-tab"><span class="label">PHASE</span><span class="num">3</span></div>
    <div class="phase-icon" style="color:#F28444"><svg viewBox="-13 -13 50 50"><use href="#people"/></svg></div>
    <div class="phase-title"><h2>Expert<br>Execution</h2><p>Where Science<br>Meets Service</p></div>
    <p class="steps-intro">Our specialized team begins the transformation process:</p>
    <ul class="steps">
      <li style="top:47px"><svg><use href="#tick"/></svg>In-depth research and analysis</li>
      <li style="top:106px"><svg><use href="#tick"/></svg>Content development and refinement</li>
      <li style="top:164px"><svg><use href="#tick"/></svg>Data interpretation and visualization</li>
      <li style="top:223px"><svg><use href="#tick"/></svg>Plain language translation of<br>complex health information</li>
    </ul>
    <svg class="wave"><use href="#wave"/></svg><span class="page-no">5</span>
    <div class="brand"><span class="dot"></span>Dr Reyes Health</div>
  </section>

  <!-- Phase 4 -->
  <section class="slide col-r" style="top:883px">
    <div class="phase-tab"><span class="label">PHASE</span><span class="num">4</span></div>
    <div class="phase-icon" style="color:#56588C"><svg viewBox="-13 -13 50 50"><use href="#people"/></svg></div>
    <div class="phase-title"><h2>Collaborative<br>Refinement</h2><p>Ensuring Perfect<br>Alignment</p></div>
    <ul class="steps">
      <li style="top:47px"><svg><use href="#tick"/></svg>Presentation of initial frameworks</li>
      <li style="top:106px"><svg><use href="#tick"/></svg>Interactive feedback sessions</li>
      <li style="top:164px"><svg><use href="#tick"/></svg>Draft review and optimization</li>
      <li style="top:223px"><svg><use href="#tick"/></svg>Stakeholder input integration</li>
    </ul>
    <svg class="wave"><use href="#wave"/></svg><span class="page-no">6</span>
    <div class="brand"><span class="dot"></span>Dr Reyes Health</div>
  </section>

  <!-- Phase 5 -->
  <section class="slide col-l" style="top:1280px">
    <div class="phase-tab"><span class="label">PHASE</span><span class="num">5</span></div>
    <div class="phase-icon" style="color:#F28444"><svg viewBox="-13 -13 50 50"><use href="#target"/></svg></div>
    <div class="phase-title"><h2>Impact<br>Delivery</h2><p>Bringing Vision<br>to Reality</p></div>
    <ul class="steps">
      <li style="top:47px"><svg><use href="#tick"/></svg>Final deliverable presentation</li>
      <li style="top:106px"><svg><use href="#tick"/></svg>Implementation support</li>
      <li style="top:164px"><svg><use href="#tick"/></svg>Knowledge transfer</li>
      <li style="top:223px"><svg><use href="#tick"/></svg>Impact measurement framework</li>
    </ul>
    <svg class="wave"><use href="#wave"/></svg><span class="page-no">7</span>
    <div class="brand"><span class="dot"></span>Dr Reyes Health</div>
  </section>

  <!-- Phase 6 -->
  <section class="slide col-r" style="top:1280px">
    <div class="phase-tab"><span class="label">PHASE</span><span class="num">6</span></div>
    <div class="phase-icon" style="color:#F24C27"><svg viewBox="-13 -13 50 50"><use href="#bulb"/></svg></div>
    <div class="phase-title"><h2>Evolution &amp;<br>Growth</h2><p>Sustaining<br>Long-term Success</p></div>
    <ul class="steps">
      <li style="top:47px"><svg><use href="#tick"/></svg>Project success celebration</li>
      <li style="top:106px"><svg><use href="#tick"/></svg>Future opportunities exploration</li>
      <li style="top:164px"><svg><use href="#tick"/></svg>Partnership evolution planning</li>
      <li style="top:223px"><svg><use href="#tick"/></svg>Continuous improvement recommendations</li>
    </ul>
    <svg class="wave"><use href="#wave"/></svg><span class="page-no">8</span>
    <div class="brand"><span class="dot"></span>Dr Reyes Health</div>
  </section>

  <!-- Why partner: wheel -->
  <section class="slide col-l why" style="top:1676px">
    <h2>Why Partner<br><span>With Us?</span></h2>
    <svg style="position:absolute;left:332px;top:86px;width:180px;height:180px" viewBox="0 0 180 180">
      <g fill="#F28444">
        <path d="M86 0A90 90 0 0 0 0 86H46A44 44 0 0 1 86 46Z"/>
        <path d="M94 0A90 90 0 0 1 180 86H134A44 44 0 0 0 94 46Z"/>
        <path d="M0 94A90 90 0 0 0 86 180V134A44 44 0 0 1 46 94Z"/>
        <path d="M180 94A90 90 0 0 1 94 180V134A44 44 0 0 0 134 94Z"/>
      </g>
      <circle cx="90" cy="90" r="28" fill="none" stroke="#3a3989" stroke-width="2"/>
      <g color="#fff">
        <use href="#people" x="28" y="28" width="24" height="24"/>
        <use href="#target" x="128" y="28" width="24" height="24"/>
        <use href="#target" x="28" y="128" width="24" height="24"/>
        <use href="#hands" x="128" y="128" width="24" height="24"/>
      </g>
    </svg>
    <div class="point right-al" style="right:294px;top:40px;width:200px"><b>Expertise:</b>Our diverse team of innovative global<br>public health professionals,<br>specialized in epidemiology and<br>health communication</div>
    <div class="point" style="left:503px;top:40px;width:110px"><b>Innovation:</b>Custom solutions<br>tailored to BIPOC<br>community needs</div>
    <div class="point right-al" style="right:294px;top:223px;width:200px"><b>Impact:</b>Proven track record of transforming<br>complex health data into<br>accessible information</div>
    <div class="point" style="left:503px;top:223px;width:110px"><b>Partnership:</b>Collaborative<br>approach ensuring<br>lasting results</div>
    <svg class="wave"><use href="#wave"/></svg><span class="page-no">9</span>
    <div class="brand"><span class="dot"></span>Dr Reyes Health</div>
  </section>

  <!-- Why partner: arc list -->
  <section class="slide col-r why why2" style="top:1676px">
    <div class="band"></div>
    <h2>Why Partner<br><span>With Us?</span></h2>
    <div class="bubble" style="left:167px;top:48px;color:#fff"><svg><use href="#people"/></svg></div>
    <div class="bubble" style="left:229px;top:114px;color:#fff"><svg><use href="#target"/></svg></div>
    <div class="bubble" style="left:229px;top:194px;color:#fff"><svg><use href="#target"/></svg></div>
    <div class="bubble" style="left:167px;top:262px;color:#fff"><svg><use href="#hands"/></svg></div>
    <div class="point" style="left:225px;top:36px;width:380px"><b>Expertise:</b>Our diverse team of innovative global public health professionals,<br>specialized in epidemiology and health communication</div>
    <div class="point" style="left:281px;top:108px;width:330px"><b>Impact:</b>Proven track record of transforming complex health<br>data into accessible information</div>
    <div class="point" style="left:281px;top:190px;width:330px"><b>Innovation:</b>Custom solutions tailored to BIPOC community needs</div>
    <div class="point" style="left:225px;top:256px;width:380px"><b>Partnership:</b>Collaborative approach ensuring lasting results</div>
    <svg class="wave"><use href="#wave"/></svg><span class="page-no">10</span>
    <div class="brand"><span class="dot"></span>Dr Reyes Health</div>
  </section>

  <!-- Closing -->
  <section class="slide col-l closing" style="top:2090px">
    <div class="arc"></div>
    <div class="logo-top"><span class="dot"></span>Dr Reyes Health</div>
    <h2>Ready<br><span>to Transform<br>Your Health<br>Communication?</span></h2>
    <p class="cta">Contact us to begin your journey toward more effective, equitable health communication.</p>
    <div class="contact"><span class="ic"><svg width="9" height="7" style="filter:invert(55%) sepia(80%) saturate(700%) hue-rotate(340deg)"><use href="#mail"/></svg></span>support@drreyeshealth.com</div>
  </section>

  <!-- Template -->
  <section class="slide col-r template" style="top:2090px">
    <h2>Presentation Title Here</h2>
    <div class="columns">
      <div class="col">
        <p><b>Lorem Ipsum</b> is simply dummy text of the printing and typesetting industry. Lorem Ipsum has been the industry's standard dummy text ever since the 1500s, when an unknown printer took a galley of type and scrambled it to make a type specimen book. It has survived not only five centuries, but also the leap into electronic typesetting.</p>
        <div class="quote"><span class="mark">“</span><span>Lorem Ipsum has been the industry's standard dummy text ever</span></div>
        <div class="quote-by">John Doe</div>
      </div>
      <div class="col">
        <p><b>Lorem Ipsum</b> is simply dummy text of the printing and typesetting industry. Lorem Ipsum has been the industry's standard dummy text ever since the 1500s, when an unknown printer took a galley of type and scrambled it to make a type specimen book. It has survived not only five centuries, but also the leap into electronic typesetting.</p>
        <div class="quote"><span class="mark">“</span><span>Lorem Ipsum has been the industry's standard dummy text ever</span></div>
        <div class="quote-by">John Doe</div>
      </div>
      <div class="col">
        <p><b>Lorem Ipsum</b> is simply dummy text of the printing and typesetting industry. Lorem Ipsum has been the industry's standard dummy text ever since the 1500s, when an unknown printer took a galley of type and scrambled it to make a type specimen book. It has survived not only five centuries, but also the leap into electronic typesetting.</p>
        <div class="quote"><span class="mark">“</span><span>Lorem Ipsum has been the industry's standard dummy text ever</span></div>
        <div class="quote-by">John Doe</div>
      </div>
    </div>
    <svg class="wave"><use href="#wave"/></svg><span class="page-no">12</span>
    <div class="brand"><span class="dot"></span>Dr Reyes Health</div>
  </section>

</div>
</body>
</html>
```